Anzeigengestaltung für einen einen ambulanten Pflegedienst
Zielgruppe
Insgesamt möchte ich gern drei Anzeigen für das Internet gestalten haben. Ich betreibe einen ambulanten Pflegedienst. Die erste Anzeige soll dazu dienen Kunden anzusprechen, die einen Unterstützungsbedarf und / oder einen Beratungsbedarf haben. Die zweite Anzeige soll dazu dienen neues Personal anzuwerben. Die dritte Anzeige soll speziell potenzielle Azubis ansprechen. Die Anzeigen sind gedacht für Chatterwall und Pixelora hauptsächlich. In den Druck sollte es schon 10cm x 8cm sein. Es wäre super wenn vielleicht auch eine Art Aufruf an ehrenamtliche Mitarbeiter erfolgt.
Aufgabenstellung
Die Anzeigen sollen den Stil der Homepage beibehalten. Freundlich, frisch und agil wirken. Alle sollten emotional ansprechend sein und gerade der für zukünftige Mitarbeiter sollte deutlich ein gutes Betriebsklima vermitteln. Als Datei habe ich einige Bilder, die bereits für die Homepage oder Flyer verwendet wurden hochgeladen. des Weiteren habe ich die einzelnen Seiten des Flyers hochgeladen.

```html
<!DOCTYPE html>
<html lang="de">
<head>
<meta charset="utf-8">
<title>Velora Pflege – Anzeigen</title>
<link href="https://fonts.googleapis.com/css2?family=Anton&family=Raleway:wght@500;600&family=Poppins:wght@400;500;600&display=swap" rel="stylesheet">
<style>
  :root{
    --board:#b9b9b9;
    --paper:#ffffff;
    --ink:#1e1e1e;
    --grey:#5b5b5b;
    --teal:#4aaea6;
    --teal-text:#3fa9a1;
    --green:#7cb342;
    --blue:#2ba3e0;
    --cross:#eeeeee;
  }
  *{box-sizing:border-box;margin:0;padding:0}
  html,body{width:1200px;height:1117px;overflow:hidden}
  body{background:var(--board);position:relative;font-family:"Poppins",sans-serif}
  .ad{position:absolute;width:543px;height:434px;background:var(--paper);overflow:hidden;box-shadow:3px 4px 8px rgba(0,0,0,.35)}
  .ad--clients{left:50px;top:121px}
  .ad--courses{left:611px;top:121px}
  .ad--jobs{left:329px;top:572px;width:553px}
  .ad__art{position:absolute;inset:0;width:100%;height:100%}
  .brand{position:absolute;left:0;width:276px;top:30px;text-align:center}
  .brand__dot{display:block;width:64px;height:64px;margin:0 auto 24px;border-radius:50%;background:var(--teal)}
  .brand__name{font-family:"Raleway",sans-serif;font-weight:500;font-size:27px;color:var(--grey);letter-spacing:.5px;white-space:nowrap}
  .ad__kicker{position:absolute;left:0;right:0;text-align:center;font-family:"Poppins",sans-serif;font-size:16px;line-height:1.2;color:var(--teal-text)}
  .ad__title{position:absolute;left:0;right:0;text-align:center;font-family:"Anton",sans-serif;font-weight:400;color:var(--ink);line-height:1;letter-spacing:.2px}
  .ad__text{position:absolute;left:40px;right:40px;text-align:center;font-size:9px;line-height:1.32;color:var(--ink)}
  .ad__url{position:absolute;left:0;right:0;bottom:6px;text-align:center;font-weight:600;font-size:11.5px;color:#fff}
  .ad--clients .ad__kicker{top:266px}
  .ad--clients .ad__title{top:290px;font-size:33px}
  .ad--clients .ad__text{top:336px}
  .ad--courses .ad__kicker{top:266px}
  .ad--courses .ad__title{top:289px;font-size:46px}
  .ad--courses .ad__text{top:342px;left:50px;right:50px}
  .ad--jobs .ad__kicker{top:264px}
  .ad--jobs .ad__title{top:288px;font-size:44px}
  .skills{position:absolute;top:340px;left:52px;right:40px;display:flex;list-style:none}
  .skills__col{padding:0 14px;border-left:1px solid #9a9a9a}
  .skills__col:first-child{border-left:0;padding-left:0}
  .skills__item{display:flex;align-items:center;gap:8px;font-size:11px;color:var(--grey);height:20px;white-space:nowrap}
  .skills__tick{width:10px;height:9px;flex:none}
</style>
</head>
<body>

<!-- Kundenanzeige -->
<section class="ad ad--clients">
  <svg class="ad__art" viewBox="0 0 724 578" preserveAspectRatio="none">
    <defs>
      <linearGradient id="photoCare" x1="0" y1="0" x2="1" y2="1">
        <stop offset="0" stop-color="#1f8f84"/><stop offset=".45" stop-color="#c9b3ad"/><stop offset="1" stop-color="#e8d7dc"/>
      </linearGradient>
    </defs>
    <path role="img" aria-label="Foto: Pflegekraft hört eine ältere Patientin mit dem Stethoskop ab" fill="url(#photoCare)" d="M318,0 H724 V360 C600,270 460,250 345,272 C362,180 335,80 318,0 Z"/>
    <path fill="var(--green)" d="M0,325 C160,245 460,220 724,340 L724,368 C460,258 170,275 0,357 Z"/>
    <path fill="var(--blue)" d="M0,368 C200,278 520,272 724,378 L724,432 C520,300 200,300 0,385 Z"/>
    <g fill="var(--cross)"><rect x="628" y="510" width="30" height="90"/><rect x="588" y="542" width="110" height="28"/><rect x="592" y="510" width="10" height="26"/><rect x="584" y="518" width="26" height="10"/></g>
    <ellipse cx="362" cy="630" rx="215" ry="112" fill="var(--teal)"/>
  </svg>
  <div class="brand"><span class="brand__dot"></span><span class="brand__name">VELORA PFLEGE</span></div>
  <p class="ad__kicker">Wir zählen auf Dich</p>
  <h2 class="ad__title">WAS WIRD AUF DICH ZUKOMMEN?</h2>
  <p class="ad__text">Die ambulante Pflege wird in der Häuslichkeit der Patienten durchgeführt. Es ist unser Ziel die Pflege für alle Beteiligten so würdevoll und respektvoll zu gestalten wie möglich. Der zu betreuende Mensch steht dabei im Vordergrund, daher gewähren wir jedem die Zeit, die er braucht.</p>
  <p class="ad__url">www.velora-pflege.de</p>
</section>

<!-- Kursanzeige -->
<section class="ad ad--courses">
  <svg class="ad__art" viewBox="0 0 724 578" preserveAspectRatio="none">
    <defs>
      <linearGradient id="photoHands" x1="0" y1="0" x2="1" y2="1">
        <stop offset="0" stop-color="#8a5a3a"/><stop offset=".5" stop-color="#c79a7c"/><stop offset="1" stop-color="#9c6a48"/>
      </linearGradient>
    </defs>
    <path role="img" aria-label="Foto: viele Hände liegen im Kreis auf einem Holztisch" fill="url(#photoHands)" d="M318,0 H724 V360 C600,270 460,250 345,272 C362,180 335,80 318,0 Z"/>
    <path fill="var(--green)" d="M0,325 C160,245 460,220 724,340 L724,368 C460,258 170,275 0,357 Z"/>
    <path fill="var(--blue)" d="M0,368 C200,278 520,272 724,378 L724,432 C520,300 200,300 0,385 Z"/>
    <g fill="var(--cross)"><rect x="628" y="510" width="30" height="90"/><rect x="588" y="542" width="110" height="28"/><rect x="592" y="510" width="10" height="26"/><rect x="584" y="518" width="26" height="10"/></g>
    <ellipse cx="362" cy="630" rx="215" ry="112" fill="var(--teal)"/>
  </svg>
  <div class="brand"><span class="brand__dot"></span><span class="brand__name">VELORA PFLEGE</span></div>
  <p class="ad__kicker">Unser Schulungsangebot für Sie</p>
  <h2 class="ad__title">PFLEGEKURSE</h2>
  <p class="ad__text">Sie sind pflegende*r Angehörige*r und möchten lernen, besser mit der Erkrankung der/des Pflegebedürftige*n umzugehen und die Pflege allgemein effektiver und belastungarmer zur gestalten? Dann sind Sie bei uns genau richtig</p>
  <p class="ad__url">www.velora-pflege.de</p>
</section>

<!-- Stellenanzeige -->
<section class="ad ad--jobs">
  <svg class="ad__art" viewBox="0 0 738 578" preserveAspectRatio="none">
    <defs>
      <linearGradient id="photoCompanion" x1="0" y1="0" x2="1" y2="1">
        <stop offset="0" stop-color="#6e6b66"/><stop offset=".5" stop-color="#d9d4cc"/><stop offset="1" stop-color="#5a4e44"/>
      </linearGradient>
    </defs>
    <path role="img" aria-label="Foto: junge Pflegerin im herzlichen Gespräch mit einer älteren Dame" fill="url(#photoCompanion)" d="M320,0 H738 V360 C610,270 470,250 350,272 C368,180 340,80 320,0 Z"/>
    <path fill="var(--green)" d="M0,325 C160,245 470,220 738,340 L738,368 C470,258 170,275 0,357 Z"/>
    <path fill="var(--blue)" d="M0,368 C200,278 530,272 738,378 L738,432 C530,300 200,300 0,385 Z"/>
    <g fill="var(--cross)"><rect x="628" y="510" width="30" height="90"/><rect x="598" y="542" width="110" height="28"/><rect x="604" y="510" width="10" height="26"/><rect x="596" y="518" width="26" height="10"/></g>
    <ellipse cx="370" cy="630" rx="215" ry="112" fill="var(--teal)"/>
  </svg>
  <div class="brand"><span class="brand__dot"></span><span class="brand__name">VELORA PFLEGE</span></div>
  <p class="ad__kicker">Wir suchen Dich!</p>
  <h2 class="ad__title">WAS BRINGST DU MIT?</h2>
  <ul class="skills">
    <li class="skills__col">
      <p class="skills__item"><svg class="skills__tick" viewBox="0 0 10 9"><path d="M1 5l3 3 5-7" fill="none" stroke="var(--green)" stroke-width="2"/></svg>Teamfähigkeit</p>
      <p class="skills__item"><svg class="skills__tick" viewBox="0 0 10 9"><path d="M1 5l3 3 5-7" fill="none" stroke="var(--green)" stroke-width="2"/></svg>Hilfsbereitschaft</p>
    </li>
    <li class="skills__col">
      <p class="skills__item"><svg class="skills__tick" viewBox="0 0 10 9"><path d="M1 5l3 3 5-7" fill="none" stroke="var(--green)" stroke-width="2"/></svg>Engagement</p>
      <p class="skills__item"><svg class="skills__tick" viewBox="0 0 10 9"><path d="M1 5l3 3 5-7" fill="none" stroke="var(--green)" stroke-width="2"/></svg>Führerschein Klasse B</p>
    </li>
    <li class="skills__col">
      <p class="skills__item"><svg class="skills__tick" viewBox="0 0 10 9"><path d="M1 5l3 3 5-7" fill="none" stroke="var(--green)" stroke-width="2"/></svg>Gute Deutschkenntnisse</p>
      <p class="skills__item"><svg class="skills__tick" viewBox="0 0 10 9"><path d="M1 5l3 3 5-7" fill="none" stroke="var(--green)" stroke-width="2"/></svg>in Wort und Schrif</p>
    </li>
  </ul>
  <p class="ad__url">www.velora-pflege.de</p>
</section>

</body>
</html>
```